Basic Company webpage with the elements and colors of our Logo

Basic Home page with a few pages:
- Home,
- About US,
- Contact us
- Services

Target Market(s)

Business Customers (B2B)

Coding

Coded - Design and coding required

Number of Pages Required

5+ page

Requirements
Must have
• Professional, Clean, Simple High Tech, Contact should have a contact us dialog for sending messages to us
Nice to have
• Meet with us links for calendar access though MS Bookings

```html
<!DOCTYPE html>
<html lang="en">
<head>
<meta charset="utf-8">
<title>Orbit Technology Services Group</title>
<link href="https://fonts.googleapis.com/css2?family=Montserrat:wght@500;600;700;800&family=Lato:wght@400;700&display=swap" rel="stylesheet">
<style>
:root{
  --navy:#0d3a58;
  --navy-deep:#0a2e47;
  --orange:#f6a623;
  --ink:#1f2a33;
  --muted:#5f6b74;
  --cream:#fdf7ee;
  --white:#ffffff;
  --line:#e3e7ea;
}
*{box-sizing:border-box;margin:0;padding:0}
html,body{width:1200px;height:3504px;overflow:hidden}
body{font-family:"Lato",Arial,sans-serif;color:var(--ink);background:var(--white);position:relative}
h1,h2,h3,h4,.nav,.btn,.brand{font-family:"Montserrat",Arial,sans-serif}
.abs{position:absolute}
.btn{display:inline-block;font-size:15px;font-weight:700;letter-spacing:.5px;color:var(--white);padding:16px 26px;border-radius:4px;background:linear-gradient(90deg,var(--navy) 0%,var(--navy) 45%,var(--orange) 100%);text-transform:uppercase}
.accent{color:var(--orange)}

/* header */
.site-header{position:absolute;top:0;left:0;width:1200px;height:100px;background:var(--white);box-shadow:0 2px 8px rgba(0,0,0,.05)}
.brand{position:absolute;left:36px;top:24px;display:flex;align-items:center;gap:12px}
.brand-dot{width:40px;height:40px;border-radius:50%;background:var(--orange);flex:none}
.brand-name{font-size:24px;font-weight:800;color:var(--navy);line-height:1;white-space:nowrap}
.brand-sub{display:block;font-size:11px;font-weight:600;letter-spacing:4px;color:var(--navy);margin-top:4px}
.nav{position:absolute;left:455px;top:36px;display:flex;gap:48px;font-size:15px;font-weight:600;color:var(--navy)}
.nav .active{color:var(--orange);border-bottom:2px solid var(--orange);padding-bottom:4px}
.site-header .btn{position:absolute;right:52px;top:22px;padding:18px 22px}

/* hero */
.hero{position:absolute;top:100px;left:0;width:1200px;height:530px;background:linear-gradient(90deg,#0d3a58 0%,#1d4f72 35%,#8aa3b6 70%,#c9d3da 100%)}
.hero-text{position:absolute;left:110px;top:120px;color:var(--white);width:500px}
.hero-text .kicker{font-family:"Montserrat",sans-serif;font-weight:700;font-size:17px;letter-spacing:1px}
.hero-text h1{font-size:42px;font-weight:800;margin-top:14px;line-height:1.05;white-space:nowrap}
.hero-text .sub{font-family:"Montserrat",sans-serif;font-weight:700;color:var(--orange);letter-spacing:4px;font-size:15px;margin-top:10px}
.hero-text p{font-size:13px;line-height:1.55;margin-top:20px;opacity:.9;width:340px}
.hero-text .btn{margin-top:28px}

/* services */
.section-title{position:absolute;left:0;width:1200px;text-align:center;font-family:"Montserrat",sans-serif;font-weight:800;font-size:40px;color:var(--navy)}
.service-card{position:absolute;top:800px;width:260px;height:460px;background:var(--white);border-radius:130px 130px 20px 20px;box-shadow:0 6px 22px rgba(0,0,0,.12);text-align:center;overflow:hidden}
.service-photo{width:200px;height:200px;border-radius:50%;margin:24px auto 0;background:linear-gradient(135deg,#a9b9c6,#e6ebef)}
.service-card h3{font-size:16px;font-weight:700;color:var(--ink);margin:18px 22px 0;line-height:1.35}
.service-card p{font-size:12px;color:var(--muted);line-height:1.55;margin:14px 22px 0}
.service-arc{position:absolute;left:0;bottom:0}
.slider-arrow{position:absolute;top:1000px;width:26px;height:26px}

/* about */
.about{position:absolute;top:1390px;left:0;width:1200px;height:570px;background:var(--navy)}
.about-photo{position:absolute;left:0;top:0;width:600px;height:500px;background:linear-gradient(135deg,#c7b9a7,#7d8c97 60%,#4a5d6c);border-radius:0 0 300px 0}
.about-text{position:absolute;left:600px;top:80px;width:520px;color:var(--white)}
.about-text h2{font-size:34px;font-weight:800}
.about-text h4{font-size:14px;letter-spacing:3px;margin-top:10px;font-weight:700}
.about-text p{font-size:13px;line-height:1.6;margin-top:16px;opacity:.9}
.btn-light{background:var(--white);color:var(--navy);padding:14px 24px;margin-top:26px}

/* testimonials */
.review{position:absolute;top:2150px;width:310px;height:200px;background:var(--white);box-shadow:0 4px 18px rgba(0,0,0,.1);border-radius:4px;padding:22px}
.review-head{display:flex;align-items:center;gap:14px}
.avatar{width:56px;height:56px;border-radius:50%;background:linear-gradient(135deg,#cfd6db,#8c9aa5)}
.stars{color:var(--orange);font-size:12px;letter-spacing:2px}
.review h4{font-size:16px;font-weight:700}
.review .date{font-size:11px;color:var(--muted)}
.review p{font-size:12px;color:var(--muted);line-height:1.55;margin-top:14px}

/* contact */
.contact{position:absolute;top:2520px;left:0;width:1200px;height:580px;background:var(--cream)}
.info{position:absolute;left:110px;display:flex;gap:22px;align-items:flex-start}
.info-icon{width:62px;height:62px;border-radius:50%;background:var(--white);box-shadow:0 3px 10px rgba(0,0,0,.08);display:flex;align-items:center;justify-content:center}
.info h4{font-size:14px;font-weight:700;color:var(--ink);margin-top:8px}
.info p{font-size:12px;color:var(--muted);line-height:1.5;margin-top:4px}
.field{position:absolute;height:52px;background:var(--white);border:1px solid var(--line);font-size:13px;color:var(--muted);padding:16px 14px}

/* footer */
.site-footer{position:absolute;top:3100px;left:0;width:1200px;height:404px;background:var(--navy-deep);color:var(--white)}
.site-footer .brand{left:110px;top:40px;gap:10px}
.site-footer .brand-dot{width:32px;height:32px}
.site-footer .brand-name{font-size:18px;color:var(--white)}
.site-footer .brand-sub{font-size:9px;letter-spacing:3px;color:var(--white)}
.socials{position:absolute;left:110px;top:130px;display:flex;gap:14px}
.socials span{width:32px;height:32px;border-radius:50%;background:var(--white)}
.f-col{position:absolute;top:40px}
.f-col h4{font-size:18px;font-weight:600;letter-spacing:.5px}
.f-col ul{list-style:none;margin-top:14px}
.f-col li{font-size:13px;line-height:2.1}
.f-contact li{display:flex;gap:12px;align-items:flex-start;line-height:1.4;margin-bottom:14px}
.pin{width:24px;height:24px;border-radius:50%;background:var(--white);flex:none}
.copyright{position:absolute;left:0;top:354px;width:1200px;text-align:center;font-size:12px;border-top:1px solid rgba(255,255,255,.2);padding-top:14px;margin:0}
</style>
</head>
<body>

<header class="site-header">
  <div class="brand"><span class="brand-dot"></span><div><span class="brand-name">ORBIT TECHNOLOGY</span><span class="brand-sub">SERVICES GROUP</span></div></div>
  <nav class="nav"><span class="active">HOME</span><span>ABOUT US</span><span>CONTACT US</span><span>SERVICES</span></nav>
  <span class="btn">Get a Quote</span>
</header>

<section class="hero" role="img" aria-label="Smiling professional woman working at a bright office desk">
  <div class="hero-text">
    <div class="kicker">WELCOME TO</div>
    <h1>ORBIT TECHNOLOGY</h1>
    <div class="sub">SERVICES GROUP</div>
    <p>Reliable managed technology for growing businesses. We plan, secure and support the systems your team depends on every single day.</p>
    <span class="btn">Meet With Us</span>
  </div>
</section>

<h2 class="section-title" style="top:705px">OUR <span class="accent">SERVICES</span></h2>

<svg class="slider-arrow abs" style="left:32px" viewBox="0 0 26 26" width="26" height="26"><circle cx="13" cy="13" r="13" fill="#1f2a33"/><path d="M15 8l-5 5 5 5" stroke="#fff" stroke-width="2" fill="none"/></svg>
<svg class="slider-arrow abs" style="left:1142px" viewBox="0 0 26 26" width="26" height="26"><circle cx="13" cy="13" r="13" fill="#1f2a33"/><path d="M11 8l5 5-5 5" stroke="#fff" stroke-width="2" fill="none"/></svg>

<article class="service-card" style="left:115px">
  <div class="service-photo" role="img" aria-label="Business handshake over a meeting table"></div>
  <h3>Lorem ipsum dolor sit amet, consectetur</h3>
  <p>Excepteur sint occaecat cupidatat non proident, sunt in culpa qui officia deserunt mollit anim id est laborum dolore magna aliqua.</p>
  <svg class="service-arc" width="260" height="70" viewBox="0 0 260 70"><path d="M0 30 Q130 -10 260 30 L260 70 L0 70Z" fill="#f6a623"/><circle cx="130" cy="40" r="13" fill="#fff"/><path d="M127 35l5 5-5 5" stroke="#f6a623" stroke-width="2.5" fill="none"/></svg>
</article>
<article class="service-card" style="left:470px">
  <div class="service-photo" role="img" aria-label="Team reviewing documents together at a desk"></div>
  <h3>Duis aute irure dolor in reprehenderit</h3>
  <p>Excepteur sint occaecat cupidatat non proident, sunt in culpa qui officia deserunt mollit anim id est laborum dolore magna aliqua.</p>
  <svg class="service-arc" width="260" height="70" viewBox="0 0 260 70"><path d="M0 30 Q130 -10 260 30 L260 70 L0 70Z" fill="#f6a623"/><circle cx="130" cy="40" r="13" fill="#fff"/><path d="M127 35l5 5-5 5" stroke="#f6a623" stroke-width="2.5" fill="none"/></svg>
</article>
<article class="service-card" style="left:825px">
  <div class="service-photo" style="background:linear-gradient(135deg,#1f4f86,#7fa5cf)" role="img" aria-label="Glass office towers seen from below"></div>
  <h3>Aliquip ex ea commodo consequat</h3>
  <p>Excepteur sint occaecat cupidatat non proident, sunt in culpa qui officia deserunt mollit anim id est laborum dolore magna aliqua.</p>
  <svg class="service-arc" width="260" height="70" viewBox="0 0 260 70"><path d="M0 30 Q130 -10 260 30 L260 70 L0 70Z" fill="#f6a623"/><circle cx="130" cy="40" r="13" fill="#fff"/><path d="M127 35l5 5-5 5" stroke="#f6a623" stroke-width="2.5" fill="none"/></svg>
</article>

<section class="about">
  <div class="about-photo" role="img" aria-label="Two colleagues smiling while working on a laptop"></div>
  <div class="about-text">
    <h2>ABOUT ORBIT TECHNOLOGY</h2>
    <h4>WHO WE ARE</h4>
    <p>At vero eos et accusamus et iusto odio dignissimos ducimus qui blanditiis praesentium voluptatum deleniti atque corrupti quos dolores et quas molestias excepturi sint occaecati cupiditate non provident, similique sunt in culpa qui officia deserunt mollitia animi, id est laborum et dolorum fuga.</p>
    <p>Nam libero tempore, cum soluta nobis est eligendi optio cumque nihil impedit quo minus id quod maxime placeat facere possimus.</p>
    <span class="btn btn-light">Read More</span>
  </div>
</section>

<h2 class="section-title" style="top:2060px">WHAT <span class="accent">CUSTOMER SAYS</span></h2>

<article class="review" style="left:100px">
  <div class="review-head"><div class="avatar" role="img" aria-label="Customer portrait"></div><div><div class="stars">★★★★★</div><h4>Daniel Harlow</h4><div class="date">March 2025</div></div></div>
  <p>Temporibus autem quibusdam et aut officiis debitis aut rerum necessitatibus saepe eveniet ut et voluptates repudiandae sint et molestiae non recusandae.</p>
</article>
<article class="review" style="left:445px">
  <div class="review-head"><div class="avatar" role="img" aria-label="Customer portrait"></div><div><div class="stars">★★★★★</div><h4>Marcus Reed</h4><div class="date">March 2025</div></div></div>
  <p>Itaque earum rerum hic tenetur a sapiente delectus, ut aut reiciendis voluptatibus maiores alias consequatur aut perferendis doloribus asperiores repellat.</p>
</article>
<article class="review" style="left:790px">
  <div class="review-head"><div class="avatar" role="img" aria-label="Customer portrait"></div><div><div class="stars">★★★★★</div><h4>Clara Benson</h4><div class="date">March 2025</div></div></div>
  <p>Nam libero tempore, cum soluta nobis est eligendi optio cumque nihil impedit quo minus id quod maxime placeat facere possimus omnis dolor.</p>
</article>
<span class="btn abs" style="left:532px;top:2405px">View More</span>

<section class="contact">
  <h2 class="section-title" style="top:100px">GET IN <span class="accent">TOUCH WITH US</span></h2>
  <div class="info" style="top:190px"><div class="info-icon"><svg width="22" height="26" viewBox="0 0 22 26"><path d="M11 1a9 9 0 0 0-9 9c0 7 9 15 9 15s9-8 9-15a9 9 0 0 0-9-9z" fill="#1f2a33"/><circle cx="11" cy="10" r="3.5" fill="#fff"/></svg></div><div><h4>ADDRESS:</h4><p>120 Maple Avenue<br>Brookfield, ST 00000</p></div></div>
  <div class="info" style="top:300px"><div class="info-icon"><svg width="22" height="22" viewBox="0 0 24 24"><path d="M6 2l4 4-2 3c1 2 4 5 6 6l3-2 4 4-3 4C10 21 3 14 2 5z" fill="#1f2a33"/></svg></div><div><h4>PHONE:</h4><p>555.010.2400</p></div></div>
  <div class="info" style="top:410px"><div class="info-icon"><svg width="24" height="18" viewBox="0 0 24 18"><rect x="1" y="1" width="22" height="16" rx="2" fill="#1f2a33"/><path d="M2 2l10 8 10-8" stroke="#fff" stroke-width="1.6" fill="none"/></svg></div><div><h4>EMAIL:</h4><p>hello@orbittechgroup.example</p></div></div>

  <div class="field" style="left:510px;top:180px;width:285px">First Name</div>
  <div class="field" style="left:810px;top:180px;width:280px">Last Name</div>
  <div class="field" style="left:510px;top:245px;width:285px">Your Phone</div>
  <div class="field" style="left:810px;top:245px;width:280px">Your Email</div>
  <div class="field" style="left:510px;top:310px;width:580px;height:115px">Message</div>
  <span class="btn abs" style="left:510px;top:445px;padding:14px 22px">Submit</span>
</section>

<footer class="site-footer">
  <div class="brand"><span class="brand-dot"></span><div><span class="brand-name">ORBIT TECHNOLOGY</span><span class="brand-sub">SERVICES GROUP</span></div></div>
  <div class="socials"><span></span><span></span><span></span><span></span></div>
  <div class="f-col" style="left:430px"><h4>QUICK LINKS</h4><ul><li>Home</li><li>About Us</li><li>Services</li><li>Contact Us</li></ul></div>
  <div class="f-col" style="left:660px"><h4>HELP LINKS</h4><ul><li>FAQ</li><li>Terms of use</li><li>Privacy Policy</li><li>Support Links</li><li>Conditions</li></ul></div>
  <div class="f-col f-contact" style="left:870px"><h4>CONTACT US</h4><ul><li><span class="pin"></span>Orbit Technology<br>United States</li><li><span class="pin"></span>+1 555 010 2400</li><li><span class="pin"></span>info@orbittech.example</li></ul></div>
  <p class="copyright">Copyright@2025 Orbit Technology All Rights Reserved</p>
</footer>

</body>
</html>
```